House-share and Room Rental Website (With Focus on the Bedroom Landing Page)

Looking for website design for our House-share (executive accommodation) and room rental business.

Our company name is: Quellnest could also be written as QuellNest or quellnest. Either is fine .. just looking for a nice clean catchy logo to go with the design.

EXAMPLES
These are examples of other websites in this field that are doing well. this is a kind of baseline.
https://dovelinter.example.au/
https://www.kestrib.example/
https://www.velunor.example/
https://www.trisbel.example/
https://www.pondmarrowseek.example.au/

Our business model is to rent rooms to people looking for high-quality accommodation. We fill the gap between those looking to rent rooms and those with rooms to rent. However, our model is slightly different from those already on the market as we looking to fill a massive gap in the market delivering upmarket rooms for rent.(Executive Accommodation) also in the back end will be coupled with a self management process in the back end.

We offer executive style accommodation that stands out above the rest. With special extras like fire safety.. and management processes that create happier homes. We are looking for a web design package that can help us grow and scale our business. We need a design that is captivating

Our MAIN focus is having a room landing page that stands out from the rest... The core of our business will rely on the promotion of the rooms in a share house... so the whole design relies on the BEDROOM landing page to drive results.

Target Market(s)

We have 2 markets we are aiming at ... the first market is people offering rooms to rent who want the highest rental return. The second market is people looking to rent safe, high-quality rooms, in houses that are well managed and looked after.

Industry/Entity Type

Share Economy

Logo Text

QuellNest

Number of Pages Required

5+ page

Font styles to use
Sans Serif

Colors
3276b5

Requirements
Must have
• A messaging system whereby we can create direct communication between those offering rooms and those looking for rooms.
• A call to action that says " Schedule an Inspection"
• Landing page for promoting rooms
• A home page for showing stock.
• Profile page for those selling rooms
• Profile page for those looking for rooms.
• A scheduling calendar for booking inspections
Nice to have
• Pages where new residents can lock in a room.. pay bond and rents.. and sign contracts
• Notifications
• SMS capabilities in the backend.
Should not have
• No script or handwriting fonts.

```html
<!DOCTYPE html>
<html lang="en">
<head>
<meta charset="utf-8">
<title>Quellnest — Explore Bedrooms</title>
<link rel="stylesheet" href="https://fonts.googleapis.com/css2?family=Archivo:wght@400;500;600;700&display=swap">
<style>
:root{
  --brand:#3276b5;
  --brand-dark:#2a639a;
  --page:#f6f8fb;
  --panel:#eef1f5;
  --ink:#262a30;
  --body:#555b63;
  --muted:#8a9099;
  --line:#dde2e8;
  --footer:#25272b;
  --footer-deep:#1c1d20;
  --white:#ffffff;
}
*{box-sizing:border-box;margin:0;padding:0}
html,body{width:1200px;height:3750px;overflow:hidden}
body{position:relative;background:var(--page);font-family:"Archivo",Arial,sans-serif;color:var(--body);font-size:12px;line-height:1.6}
.abs{position:absolute}
h2.section-title{font-size:30px;font-weight:600;color:var(--ink);letter-spacing:.2px}
a{color:var(--brand);text-decoration:none}

/* hero */
.hero{left:0;top:0;width:1200px;height:578px}
.hero-photo{left:420px;top:0;width:780px;height:578px;background:linear-gradient(100deg,#6b5444 0%,#a8927c 30%,#e8e3da 55%,#cdbfae 75%,#5e4b3d 100%)}
.hero-panel{left:0;top:0;width:420px;height:578px;background:var(--panel)}
.topbar{left:0;top:0;width:1200px;height:62px}
.logo{left:24px;top:14px;display:flex;align-items:center;gap:8px;color:var(--white);font-size:22px;font-weight:500}
.logo .mark{width:16px;height:16px;border:2px solid var(--white);border-radius:50%}
.search{left:235px;top:10px;width:345px;height:36px;background:var(--white);border-radius:3px;display:flex;align-items:center;padding-left:14px;gap:8px;color:var(--ink);font-size:14px}
.nav{right:24px;top:18px;display:flex;gap:26px;color:var(--white);font-size:13px}
.slide-arrow{width:36px;height:40px;background:rgba(255,255,255,.85);display:flex;align-items:center;justify-content:center}
.hero-title{left:40px;top:84px;font-size:30px;font-weight:600;color:var(--ink)}
.hero-lede{left:40px;top:134px;width:360px;font-size:13px;line-height:1.5;color:var(--body)}
.hero-link{left:40px;top:190px;font-size:12px}
.facts{left:40px;top:230px;width:360px;border-collapse:collapse;font-size:12px;color:var(--ink)}
.facts td{height:21.5px;padding:0}
.facts td:first-child{width:115px}
.btn{display:inline-flex;align-items:center;justify-content:center;background:var(--brand);color:var(--white);font-weight:500;border-radius:2px}
.hero-cta{left:40px;top:476px;width:180px;height:40px;font-size:13px}

/* host */
.host-title{left:172px;top:622px;font-size:28px;font-weight:600;color:var(--ink)}
.host-name{left:172px;top:660px;font-size:13px;color:var(--body)}
.avatar{background:linear-gradient(135deg,#9aa3ad,#5c6670);border-radius:2px}
.host-avatar{left:330px;top:625px;width:52px;height:52px;background:linear-gradient(135deg,#b04a6a,#3b2430)}
.host-text{left:172px;top:702px;width:858px;font-size:12px;line-height:1.7}
.host-login{left:172px;top:802px;font-size:13px}

/* description */
.desc-title{left:172px;top:862px}
.desc-text{left:172px;top:912px;width:410px;font-size:12px;line-height:1.7}
.desc-text p+p{margin-top:14px}
.desc-photo{left:610px;top:900px;width:420px;height:255px;background:linear-gradient(180deg,#d7e6f2 0%,#c8ccd0 45%,#6f6b66 70%,#4d7a3f 100%)}
.rent-title{left:172px;top:1136px;font-size:13px;font-weight:600;color:var(--ink)}
.rent-table{left:172px;top:1166px;font-size:12px;color:var(--ink)}
.rent-table td{height:26px;padding-right:28px}

/* amenities */
.amen-title{left:172px;top:1318px}
.amen-link{left:440px;top:1334px;font-size:13px;text-decoration:underline}
.amen-box{left:172px;top:1388px;width:858px;height:182px;background:#ecedef;border:1px solid var(--line);display:flex;justify-content:space-around;align-items:center;padding:0 40px}
.amen-item{display:flex;flex-direction:column;align-items:center;gap:14px;font-size:12px;color:var(--ink)}
.amen-more{left:172px;top:1612px;font-size:13px}

/* availability */
.avail-title{left:172px;top:1662px}
.avail-row{left:172px;top:1737px;width:858px;display:flex;gap:9px}
.field{height:38px;background:var(--brand);color:var(--white);font-size:13px;display:flex;align-items:center;justify-content:space-between;padding:0 12px;border-radius:2px}

/* public amenities */
.pub-title{left:172px;top:1858px}
.pub-text{left:172px;top:1918px;width:568px;font-size:12px;line-height:1.7}
.pub-list{left:765px;top:1918px;display:flex;flex-direction:column;gap:20px;font-size:12px;color:var(--ink)}
.pub-list li{list-style:none;display:flex;align-items:center;gap:14px}
.map{left:172px;top:2093px;width:858px;height:422px;background:linear-gradient(135deg,#e6e9e4 0%,#dfe4dc 40%,#ebe7dd 70%,#e2e6ea 100%)}

/* reviews */
.rev-title{left:172px;top:2555px}
.rev-rule{left:172px;top:2605px;width:858px;height:1px;background:var(--line)}
.review{width:420px}
.review .who{display:flex;gap:12px;align-items:center}
.review .av{width:44px;height:44px}
.review .name{font-size:14px;color:var(--ink);font-weight:500}
.review .date{font-size:11px;color:var(--muted)}
.review p{margin-top:14px;font-size:12px;line-height:1.7}
.rev-all{left:172px;top:2928px;font-size:13px}

/* see also */
.see-title{left:172px;top:2993px}
.card{width:222px;text-align:center}
.card .photo{height:225px}
.card h3{margin-top:12px;font-size:13px;font-weight:600;color:var(--ink);line-height:1.35}
.card .price{margin-top:10px;width:150px;height:28px;font-size:12px}
.carousel-btn{width:44px;height:54px;background:var(--brand);display:flex;align-items:center;justify-content:center}

/* footer */
.footer{left:0;top:3432px;width:1200px;height:318px;background:var(--footer);color:#c9ccd1}
.footer h4{font-size:17px;font-weight:600;color:var(--white)}
.footer .underline{width:34px;height:2px;background:var(--white);margin-top:8px}
.f-about{left:172px;top:50px;width:260px}
.f-about p{margin-top:22px;font-size:11px;line-height:1.7}
.socials{display:flex;gap:10px;margin-top:14px;justify-content:center}
.socials span{width:10px;height:10px;border-radius:50%;background:#c9ccd1}
.f-links{left:515px;top:50px}
.f-links ul{list-style:none;font-size:12px;line-height:1.75;margin-top:22px}
.f-links .cols{display:flex;gap:50px}
.f-news{left:760px;top:50px;width:270px}
.f-news p{margin-top:22px;font-size:11px}
.f-news .input{margin-top:12px;height:32px;background:var(--white);color:var(--muted);font-size:12px;display:flex;align-items:center;padding-left:12px}
.f-news .btn{margin-top:8px;width:100%;height:30px;font-size:12px}
.f-bottom{left:0;top:268px;width:1200px;height:50px;background:var(--footer-deep);font-size:11px;display:flex;align-items:center;padding-left:24px}
.to-top{right:170px;top:282px;width:24px;height:22px;background:var(--brand);display:flex;align-items:center;justify-content:center}
</style>
</head>
<body>

<!-- Hero -->
<section class="abs hero">
  <div class="abs hero-photo" role="img" aria-label="Photo of a furnished bedroom with striped walls and a made double bed"></div>
  <div class="abs hero-panel"></div>
  <div class="abs slide-arrow" style="left:422px;top:292px"><svg width="10" height="14" viewBox="0 0 10 14"><path d="M8 1L2 7l6 6" fill="none" stroke="#333" stroke-width="2"/></svg></div>
  <div class="abs slide-arrow" style="left:1160px;top:292px"><svg width="10" height="14" viewBox="0 0 10 14"><path d="M2 1l6 6-6 6" fill="none" stroke="#333" stroke-width="2"/></svg></div>
  <div class="abs topbar">
    <div class="abs logo"><span class="mark"></span>Quellnest</div>
    <div class="abs search"><svg width="13" height="13" viewBox="0 0 14 14"><circle cx="6" cy="6" r="4.5" fill="none" stroke="#333" stroke-width="1.6"/><path d="M9.5 9.5L13 13" stroke="#333" stroke-width="1.6"/></svg>Search</div>
    <nav class="abs nav"><span>Become a host</span><span>Profile</span><span>Sign up</span><span>Log in</span></nav>
  </div>
  <h1 class="abs hero-title">Explore Bedrooms</h1>
  <p class="abs hero-lede">Nam libero tempore, cum soluta nobis est eligendi optio cumque nihil impedit quo minus id.</p>
  <a class="abs hero-link">Excellent Location · Show Map</a>
  <table class="abs facts">
    <tr><td>Gender</td><td>Couple</td></tr>
    <tr><td>Bedroom Size</td><td>Large bedroom (queen sized bed)</td></tr>
    <tr><td>Bathroom</td><td>Private</td></tr>
    <tr><td>Housemates</td><td>Professionals</td></tr>
    <tr><td>Room type</td><td>Private</td></tr>
    <tr><td>Internet speed</td><td>High Speed</td></tr>
    <tr><td>Minimum contract</td><td>6 Months</td></tr>
    <tr><td>Parking</td><td>Private</td></tr>
    <tr><td>Smoking</td><td>Non Smoking</td></tr>
  </table>
  <span class="abs btn hero-cta">Schedule an Inspection</span>
</section>

<!-- Host -->
<h2 class="abs host-title">Your Host</h2>
<div class="abs host-name">Liora Fenwick</div>
<div class="abs avatar host-avatar" role="img" aria-label="Host profile photo"></div>
<p class="abs host-text">Sed ut perspiciatis unde omnis iste natus error sit voluptatem accusantium doloremque laudantium, totam rem aperiam, eaque ipsa quae ab illo inventore veritatis et quasi architecto beatae vitae dicta sunt explicabo. Nemo enim ipsam voluptatem quia voluptas sit aspernatur aut odit aut fugit, sed quia consequuntur magni dolores eos qui ratione voluptatem sequi nesciunt. Neque porro quisquam est, qui dolorem ipsum quia dolor sit amet, consectetur.</p>
<a class="abs host-login">Login to Message Host</a>

<!-- Description -->
<h2 class="abs section-title desc-title">Description</h2>
<div class="abs desc-text">
  <p>Nemo enim ipsam voluptatem quia voluptas sit aspernatur aut odit aut fugit, sed quia consequuntur magni dolores eos qui ratione voluptatem sequi nesciunt. Neque porro quisquam est, qui dolorem ipsum quia dolor sit amet, consectetur, adipisci velit sed quia non numquam eius modi tempora incidunt ut labore et dolore magnam aliquam quaerat voluptatem.</p>
  <p>Quis autem vel eum iure reprehenderit qui in ea voluptate velit esse quam nihil molestiae consequatur, vel illum qui dolorem eum fugiat quo voluptas nulla pariatur excepteur sint occaecat maiores alias consequatur aut perferendis doloribus asperiores repellat.</p>
</div>
<div class="abs desc-photo" role="img" aria-label="Photo of a modern two-storey house exterior with lawn"></div>
<div class="abs slide-arrow" style="left:612px;top:1008px;width:26px;height:30px"><svg width="8" height="12" viewBox="0 0 10 14"><path d="M8 1L2 7l6 6" fill="none" stroke="#333" stroke-width="2"/></svg></div>
<div class="abs slide-arrow" style="left:1002px;top:1008px;width:26px;height:30px"><svg width="8" height="12" viewBox="0 0 10 14"><path d="M2 1l6 6-6 6" fill="none" stroke="#333" stroke-width="2"/></svg></div>
<div class="abs rent-title">Rent, Bills and Expenses</div>
<table class="abs rent-table">
  <tr><td>Rent</td><td>$500 PW ($1,100 per calendar month) Bond: $1100</td></tr>
  <tr><td>Bill</td><td>All bills are shared 50/50</td></tr>
</table>

<!-- Room amenities -->
<h2 class="abs section-title amen-title">Room Amenities</h2>
<a class="abs amen-link">All Rooms Include</a>
<div class="abs amen-box">
  <div class="amen-item"><svg width="48" height="44" viewBox="0 0 48 44" fill="none" stroke="#3276b5" stroke-width="2"><rect x="4" y="18" width="30" height="12"/><path d="M4 30v8M34 30v8M10 18V8h18v10"/><rect x="36" y="6" width="8" height="32"/></svg>Furnished</div>
  <div class="amen-item"><svg width="48" height="44" viewBox="0 0 48 44" fill="none" stroke="#3276b5" stroke-width="2"><rect x="6" y="12" width="36" height="24" rx="2"/><path d="M18 4l6 8 6-8M16 40h16"/></svg>TV</div>
  <div class="amen-item"><svg width="48" height="44" viewBox="0 0 48 44" fill="none" stroke="#3276b5" stroke-width="2"><rect x="14" y="4" width="20" height="36"/><path d="M14 13h20M14 22h20M14 31h20"/></svg>Storage Space</div>
  <div class="amen-item"><svg width="48" height="44" viewBox="0 0 48 44" fill="none" stroke="#3276b5" stroke-width="2"><path d="M4 24h40M8 24v16M40 24v16"/><rect x="14" y="8" width="18" height="12"/><path d="M23 20v4"/></svg>Study Desk</div>
  <div class="amen-item"><svg width="48" height="44" viewBox="0 0 48 44" fill="none" stroke="#3276b5" stroke-width="2"><rect x="10" y="4" width="28" height="36"/><path d="M24 4v36M20 20v4M28 20v4"/></svg>Wardrobe</div>
  <div class="amen-item"><svg width="48" height="44" viewBox="0 0 48 44" fill="none" stroke="#3276b5" stroke-width="2"><path d="M12 40V10a6 6 0 0 1 12 0v2"/><path d="M18 12h12l-2 6H20z"/><path d="M22 24v4M26 24v6M30 24v4"/></svg>Ensuite Shower</div>
  <div class="amen-item"><svg width="48" height="44" viewBox="0 0 48 44" fill="none" stroke="#3276b5" stroke-width="2"><rect x="6" y="6" width="36" height="32"/><path d="M6 16h36M24 16v22"/><circle cx="14" cy="11" r="2"/><circle cx="22" cy="11" r="2"/></svg>Kitchenette</div>
</div>
<a class="abs amen-more">+ Show More Amenities</a>

<!-- Availability -->
<h2 class="abs section-title avail-title">Check Availability</h2>
<div class="abs avail-row">
  <div class="field" style="width:173px">Check-in date<svg width="12" height="12" viewBox="0 0 12 12" fill="none" stroke="#fff" stroke-width="1.3"><rect x="1" y="2" width="10" height="9"/><path d="M1 5h10M4 1v2M8 1v2"/></svg></div>
  <div class="field" style="width:173px">Check-out date<svg width="12" height="12" viewBox="0 0 12 12" fill="none" stroke="#fff" stroke-width="1.3"><rect x="1" y="2" width="10" height="9"/><path d="M1 5h10M4 1v2M8 1v2"/></svg></div>
  <div class="field" style="width:173px">Guests<svg width="10" height="6" viewBox="0 0 10 6"><path d="M0 0h10L5 6z" fill="#fff"/></svg></div>
  <div class="field" style="width:173px;justify-content:center">Submit</div>
  <div class="field" style="width:130px;justify-content:center">Change Search</div>
</div>

<!-- Public amenities -->
<h2 class="abs section-title pub-title">Public Amenities</h2>
<p class="abs pub-text">Neque porro quisquam est, qui dolorem ipsum quia dolor sit amet, consectetur, adipisci velit sed quia non numquam eius modi tempora incidunt ut labore et dolore magnam aliquam quaerat voluptatem. Quis autem vel eum iure reprehenderit qui in ea voluptate velit esse quam nihil molestiae consequatur. Nam libero tempore, cum soluta nobis est eligendi optio cumque nihil impedit quo minus id quod maxime placeat facere possimus, omnis voluptas assumenda est, omnis dolor repellendus.</p>
<ul class="abs pub-list">
  <li><svg width="22" height="22" viewBox="0 0 22 22" fill="none" stroke="#3276b5" stroke-width="1.6"><rect x="4" y="2" width="14" height="15" rx="2"/><path d="M4 10h14M7 20l2-3M15 20l-2-3"/></svg>09 mins by car without traffic</li>
  <li><svg width="22" height="22" viewBox="0 0 22 22" fill="none" stroke="#3276b5" stroke-width="1.6"><path d="M2 12l18-8-6 16-3-6z"/></svg>09 mins by car without traffic</li>
  <li><svg width="22" height="22" viewBox="0 0 22 22" fill="none" stroke="#3276b5" stroke-width="1.6"><rect x="1" y="6" width="20" height="10" rx="2"/><circle cx="6" cy="17" r="1.5"/><circle cx="16" cy="17" r="1.5"/></svg>5 mins walking distance</li>
</ul>
<div class="abs map" role="img" aria-label="Street map of the area around the property"></div>

<!-- Reviews -->
<h2 class="abs section-title rev-title">Reviews</h2>
<div class="abs rev-rule"></div>
<article class="abs review" style="left:172px;top:2630px">
  <div class="who"><div class="av avatar"></div><div><div class="name">Maren Holt</div><div class="date">11th Feb,2018</div></div></div>
  <p>Nam libero tempore, cum soluta nobis est eligendi optio cumque nihil impedit quo minus id quod maxime placeat facere possimus, omnis voluptas assumenda est omnis dolor repellendus.</p>
</article>
<article class="abs review" style="left:610px;top:2630px">
  <div class="who"><div class="av avatar"></div><div><div class="name">Teodor Crane</div><div class="date">11th Feb,2018</div></div></div>
  <p>Nam libero tempore, cum soluta nobis est eligendi optio cumque nihil impedit quo minus id quod maxime placeat facere possimus, omnis voluptas assumenda est omnis dolor repellendus.</p>
</article>
<article class="abs review" style="left:172px;top:2800px">
  <div class="who"><div class="av avatar"></div><div><div class="name">Alder Quist</div><div class="date">11th Feb,2018</div></div></div>
  <p>Nam libero tempore, cum soluta nobis est eligendi optio cumque nihil impedit quo minus id quod maxime placeat facere possimus, omnis voluptas assumenda est omnis dolor repellendus.</p>
</article>
<article class="abs review" style="left:610px;top:2800px">
  <div class="who"><div class="av avatar"></div><div><div class="name">Ilse Marrow</div><div class="date">11th Feb,2018</div></div></div>
  <p>Nam libero tempore, cum soluta nobis est eligendi optio cumque nihil impedit quo minus id quod maxime placeat facere possimus, omnis voluptas assumenda est omnis dolor repellendus.</p>
</article>
<a class="abs rev-all">View All Reviews</a>

<!-- See also -->
<h2 class="abs section-title see-title">See Also</h2>
<div class="abs carousel-btn" style="left:172px;top:3165px"><svg width="10" height="14" viewBox="0 0 10 14"><path d="M8 1L2 7l6 6" fill="none" stroke="#fff" stroke-width="2"/></svg></div>
<div class="abs carousel-btn" style="left:978px;top:3165px"><svg width="10" height="14" viewBox="0 0 10 14"><path d="M2 1l6 6-6 6" fill="none" stroke="#fff" stroke-width="2"/></svg></div>
<article class="abs card" style="left:250px;top:3075px">
  <div class="photo" role="img" aria-label="Photo of a warm lit bedroom with a double bed" style="background:linear-gradient(160deg,#3a2e28,#8a6e58 55%,#d9cbbb)"></div>
  <h3>Recusandis Voluptatibus Molores Alias Consequatur</h3>
  <span class="btn price">$350 per week</span>
</article>
<article class="abs card" style="left:489px;top:3075px">
  <div class="photo" role="img" aria-label="Photo of a grey toned bedroom with a low bed" style="background:linear-gradient(160deg,#6d6a68,#b7b2ab 55%,#e6e2dc)"></div>
  <h3>Quis Minus Quod Maxime aut Placeat Facere</h3>
  <span class="btn price">$600 per week</span>
</article>
<article class="abs card" style="left:728px;top:3075px">
  <div class="photo" role="img" aria-label="Photo of a bright white bedroom with a chandelier" style="background:linear-gradient(160deg,#c9c6c2,#eeebe6 55%,#9b948c)"></div>
  <h3>Quis Nostrum Exercitationem Ullam Corporis Suscipit</h3>
  <span class="btn price">$1000 per week</span>
</article>

<!-- Footer -->
<footer class="abs footer">
  <div class="abs f-about">
    <h4>About Us</h4><div class="underline"></div>
    <p>Quis autem vel eum iure reprehenderit qui in ea voluptate velit esse quam nihil molestiae consequatur, vel illum qui dolorem eum fugiat quo voluptas nulla pariatur.</p>
    <div class="socials"><span></span><span></span><span></span><span></span></div>
  </div>
  <div class="abs f-links">
    <h4>Links</h4><div class="underline"></div>
    <div class="cols">
      <ul><li>Sign up</li><li>Log in</li><li>Pricing</li><li>Contact Us</li></ul>
      <ul><li>Trust · Safety</li><li>Travel Credit</li><li>Guidebooks</li><li>Reviews</li></ul>
    </div>
  </div>
  <div class="abs f-news">
    <h4>Newsletter</h4><div class="underline"></div>
    <p>Subscribe to our newsletter for latest updates</p>
    <div class="input">Email...</div>
    <span class="btn">Subscribe</span>
  </div>
  <div class="abs f-bottom">©Copyright information here</div>
  <div class="abs to-top"><svg width="10" height="6" viewBox="0 0 10 6"><path d="M5 0l5 6H0z" fill="#fff"/></svg></div>
</footer>

</body>
</html>
```